Business card design needed

I would like a one sided black business card with the information provided above. Refer to my website www.lobcrafttennis.com.au for an example of colors I have used for my site, would like to keep this consistent for my business cards also, I will upload my logo below.

I am a new small business that provides tennis customers with racquet re stringing, tennis strings and accessories.

Industry/Entity Type

Small Business

Contact Information for Business Card

Lob Craft Tennis

Dennis Morrow
Managing Director

lobcrafttennis@mailbay.com
www.lobcrafttennis.com.au
0412 695 203

Racquet Restringing/Tennis Strings/Accessories

Requirements
Must have
• Must have my logo and card must be black

```html
<!DOCTYPE html>
<html lang="en">
<head>
<meta charset="utf-8">
<title>Lob Craft Tennis – Business Card</title>
<link rel="stylesheet" href="https://fonts.googleapis.com/css2?family=Cabin:ital,wght@0,400;0,600;1,400&display=swap">
<style>
  :root {
    --page-bg: #2b2b2b;
    --card-black: #080808;
    --card-glow: #2e2e2e;
    --lime: #b9d535;
    --white: #f4f4f4;
    --soft-grey: #c9c9c9;
    --bullet-blue: #4f8fd0;
    --link-blue: #1d3c8c;
  }
  * { box-sizing: border-box; margin: 0; padding: 0; }
  html, body {
    width: 1200px;
    height: 949px;
    overflow: hidden;
    background: var(--page-bg);
    font-family: "Cabin", "Gill Sans", sans-serif;
  }
  .business-card {
    position: absolute;
    left: 80px;
    top: 181px;
    width: 1040px;
    height: 587px;
    background: radial-gradient(ellipse 70% 75% at 50% 12%, var(--card-glow) 0%, #141414 55%, var(--card-black) 100%);
    box-shadow: 0 14px 40px rgba(0,0,0,0.55);
    overflow: hidden;
  }
  .brand {
    position: absolute;
    left: 82px;
    top: 150px;
    display: flex;
    align-items: center;
    gap: 18px;
  }
  .brand-dot {
    width: 40px;
    height: 40px;
    border-radius: 50%;
    background: var(--lime);
  }
  .brand-name {
    color: var(--lime);
    font-size: 52px;
    font-weight: 600;
    letter-spacing: 0.5px;
  }
  .contact {
    position: absolute;
    right: 82px;
    top: 92px;
    text-align: right;
  }
  .contact-name {
    color: var(--white);
    font-size: 42px;
    font-weight: 400;
    line-height: 1.1;
  }
  .contact-role {
    color: var(--lime);
    font-size: 27px;
    font-style: italic;
    line-height: 1.2;
  }
  .contact-email {
    margin-top: 68px;
    color: var(--soft-grey);
    font-size: 29px;
  }
  .contact-phone {
    margin-top: 12px;
    display: flex;
    justify-content: flex-end;
    align-items: center;
    gap: 18px;
    color: var(--soft-grey);
    font-size: 38px;
    letter-spacing: 1px;
  }
  .phone-icon { width: 48px; height: 48px; }
  .services {
    position: absolute;
    left: 78px;
    top: 345px;
    list-style: none;
  }
  .services li {
    display: flex;
    align-items: center;
    gap: 18px;
    color: var(--white);
    font-size: 31px;
    font-style: italic;
    line-height: 41px;
  }
  .services li::before {
    content: "";
    width: 17px;
    height: 17px;
    border-radius: 50%;
    background: radial-gradient(circle at 35% 35%, #bfe0ff 0%, var(--bullet-blue) 55%, #1d4f8a 100%);
  }
  .web-band {
    position: absolute;
    left: 0;
    bottom: 0;
    width: 100%;
    height: 70px;
    background: var(--lime);
    display: flex;
    justify-content: flex-end;
    align-items: center;
    padding-right: 60px;
  }
  .web-address {
    color: var(--link-blue);
    font-size: 28px;
  }
</style>
</head>
<body>
  <div class="business-card">
    <div class="brand">
      <span class="brand-dot"></span>
      <span class="brand-name">Lob Craft Tennis</span>
    </div>

    <div class="contact">
      <p class="contact-name">Dennis Morrow</p>
      <p class="contact-role">Managing Director</p>
      <p class="contact-email">lobcrafttennis@mailbay.com</p>
      <p class="contact-phone">
        <span>0412 695 203</span>
        <svg class="phone-icon" viewBox="0 0 48 48" aria-hidden="true">
          <circle cx="24" cy="24" r="21" fill="none" stroke="#c9c9c9" stroke-width="2.5"/>
          <path d="M17 13c-2 1-3 3-2 6 2 7 7 12 14 15 3 1 5 0 6-2l1-2-5-4-3 2c-3-1-6-4-7-7l2-3-4-5z" fill="#c9c9c9"/>
        </svg>
      </p>
    </div>

    <ul class="services">
      <li>Racquet Restringing</li>
      <li>Tennis Strings</li>
      <li>Accessories</li>
    </ul>

    <div class="web-band">
      <span class="web-address">www.lobcrafttennis.com.au</span>
    </div>
  </div>
</body>
</html>
```